Dockhavenly is a new company, currently under development opening in June. We store & repair shi

This is our first draft of what we want to present & it is very basic.
Our clients are shipping lines and we would like something with a bit of flair. We had the logo designed so those colours of yellow & grey are non negotiable. We are looking for background colours, heading designs etc to blend in whilst incorporating an image of sustainability, moving forward into the future and offering professional service.

Industry/Entity Type

Shipping

```html
<!DOCTYPE html>
<html lang="en">
<head>
<meta charset="UTF-8">
<title>Dockhavenly – Contents</title>
<link rel="stylesheet" href="https://fonts.googleapis.com/css2?family=Old+Standard+TT&family=Saira+Semi+Condensed:wght@400;500;600&display=swap">
<style>
  :root {
    --yellow: #f9b80f;
    --slate: #3a4853;
    --box-grey: #7a7a7a;
    --accent-grey: #6e6e6e;
    --text-dark: #3b3b3b;
    --white: #ffffff;
  }
  * { margin: 0; padding: 0; box-sizing: border-box; }
  html, body { width: 1200px; height: 900px; overflow: hidden; background: var(--white); }
  .slide {
    position: relative;
    width: 1200px;
    height: 900px;
    font-family: "Saira Semi Condensed", sans-serif;
    color: var(--text-dark);
  }
  .title-marker {
    position: absolute; left: 0; top: 30px;
    width: 15px; height: 67px;
    background: var(--accent-grey);
  }
  .project-title {
    position: absolute; left: 27px; top: 30px;
    font-family: "Old Standard TT", serif;
    font-weight: 400;
    font-size: 47px;
    line-height: 64px;
    color: var(--slate);
    letter-spacing: 0.5px;
  }
  .project-title .highlight { color: var(--yellow); }
  .brand {
    position: absolute; right: 18px; top: 24px;
    display: flex; align-items: center; gap: 12px;
  }
  .brand-square { width: 26px; height: 26px; background: var(--slate); }
  .brand-name {
    font-size: 52px; font-weight: 600; line-height: 1;
    color: var(--yellow);
  }
  .agenda-item {
    position: absolute;
    display: flex; align-items: center;
    height: 71px;
  }
  .agenda-number {
    height: 71px; width: 80px;
    border-left: 5px solid var(--yellow);
    padding-left: 3px;
    background: linear-gradient(to right, var(--white) 0 3px, var(--box-grey) 3px);
    color: var(--white);
    font-size: 39px; font-weight: 400;
    display: flex; align-items: center; justify-content: center;
    padding-left: 6px;
  }
  .agenda-title {
    margin-left: 20px;
    font-size: 32px; font-weight: 400;
    color: var(--text-dark);
  }
  .col-left { left: 27px; }
  .col-right { left: 610px; }
  .footer-stripe {
    position: absolute; left: 0; top: 805px;
    width: 1200px; height: 15px; background: var(--yellow);
  }
  .footer {
    position: absolute; left: 0; top: 820px;
    width: 1200px; height: 80px; background: var(--slate);
    color: var(--white);
  }
  .copyright {
    position: absolute; left: 37px; top: 26px;
    font-size: 22px; font-weight: 400;
  }
  .page-number {
    position: absolute; right: 22px; top: 22px;
    font-size: 29px; font-weight: 600;
  }
</style>
</head>
<body>
<div class="slide">
  <div class="title-marker"></div>
  <h1 class="project-title"><span class="highlight">PROJECT</span> TITLE HERE</h1>

  <div class="brand">
    <span class="brand-square"></span>
    <span class="brand-name">Dockhavenly</span>
  </div>

  <div class="agenda-item col-left" style="top:148px"><span class="agenda-number">01</span><span class="agenda-title">Slide Title Here</span></div>
  <div class="agenda-item col-left" style="top:255px"><span class="agenda-number">02</span><span class="agenda-title">Slide Title Here</span></div>
  <div class="agenda-item col-left" style="top:370px"><span class="agenda-number">03</span><span class="agenda-title">Slide Title Here</span></div>
  <div class="agenda-item col-left" style="top:489px"><span class="agenda-number">04</span><span class="agenda-title">Slide Title Here</span></div>
  <div class="agenda-item col-left" style="top:597px"><span class="agenda-number">05</span><span class="agenda-title">Slide Title Here</span></div>

  <div class="agenda-item col-right" style="top:148px"><span class="agenda-number">06</span><span class="agenda-title">Slide Title Here</span></div>
  <div class="agenda-item col-right" style="top:255px"><span class="agenda-number">07</span><span class="agenda-title">Slide Title Here</span></div>
  <div class="agenda-item col-right" style="top:370px"><span class="agenda-number">08</span><span class="agenda-title">Slide Title Here</span></div>
  <div class="agenda-item col-right" style="top:489px"><span class="agenda-number">09</span><span class="agenda-title">Slide Title Here</span></div>
  <div class="agenda-item col-right" style="top:597px"><span class="agenda-number">10</span><span class="agenda-title">Slide Title Here</span></div>

  <div class="footer-stripe"></div>
  <footer class="footer">
    <span class="copyright">Copyright text here</span>
    <span class="page-number">1</span>
  </footer>
</div>
</body>
</html>
```